Biz Cards to match new logo

I'm looking for a business card layout to go with my new logo. I'd like to have one side in colour (purple, with the logo in white) and the other side to be white with the purple logo and contact info in black font: name, address (2 lines), phone, email, fax, website. The logo includes the company name so it doesn't need to be repeated in the text. The font should be legibile to the semi-blind. (I hate small fonts on business cards).

```html
<!DOCTYPE html>
<html lang="en">
<head>
<meta charset="utf-8">
<title>Corvane Research – Business Cards</title>
<link rel="stylesheet" href="https://fonts.googleapis.com/css2?family=Open+Sans:wght@400;600&display=swap">
<style>
  :root {
    --brand-purple: #6a4088;
    --paper-white: #ffffff;
    --ink-black: #1e1e1e;
    --backdrop: #d4d4d4;
  }
  * { box-sizing: border-box; margin: 0; padding: 0; }
  html, body {
    width: 1200px;
    height: 985px;
    overflow: hidden;
    background: var(--backdrop);
    font-family: "Open Sans", Arial, sans-serif;
  }
  .canvas {
    position: relative;
    width: 1200px;
    height: 985px;
  }
  .card {
    position: absolute;
    left: 320px;
    width: 560px;
    height: 320px;
    border-radius: 22px;
    overflow: hidden;
  }
  .card--back {
    top: 120px;
    background: var(--brand-purple);
    display: flex;
    align-items: center;
    justify-content: center;
  }
  .card--front {
    top: 515px;
    background: var(--paper-white);
  }
  .wordmark {
    display: flex;
    align-items: center;
    gap: 14px;
    font-weight: 600;
    font-size: 34px;
    letter-spacing: 2px;
    line-height: 1;
  }
  .wordmark__square {
    width: 30px;
    height: 30px;
  }
  .card--back .wordmark { color: var(--paper-white); }
  .card--back .wordmark__square { background: var(--paper-white); }
  .card--front .wordmark {
    position: absolute;
    left: 34px;
    top: 92px;
    flex-direction: column;
    align-items: flex-start;
    gap: 10px;
    font-size: 28px;
    color: var(--brand-purple);
  }
  .card--front .wordmark__square { background: var(--brand-purple); }
  .contact {
    position: absolute;
    left: 300px;
    top: 52px;
    color: var(--ink-black);
  }
  .contact__name {
    font-size: 20px;
    font-weight: 400;
    color: var(--brand-purple);
    line-height: 1.1;
  }
  .contact__title {
    font-size: 13px;
    color: var(--brand-purple);
    margin-bottom: 8px;
  }
  .contact__address {
    font-size: 16px;
    line-height: 1.2;
    margin-bottom: 10px;
  }
  .contact__list { list-style: none; }
  .contact__item {
    display: flex;
    align-items: center;
    gap: 10px;
    font-size: 16px;
    line-height: 1.45;
  }
  .contact__icon {
    width: 16px;
    height: 16px;
    flex: none;
  }
  .front-band {
    position: absolute;
    left: 0;
    bottom: 0;
    width: 560px;
    height: 40px;
  }
</style>
</head>
<body>
<main class="canvas">

  <section class="card card--back" aria-label="Card back">
    <div class="wordmark">
      <span class="wordmark__square"></span>
      <span class="wordmark__name">CORVANE RESEARCH</span>
    </div>
  </section>

  <section class="card card--front" aria-label="Card front">
    <div class="wordmark">
      <span class="wordmark__square"></span>
      <span class="wordmark__name">CORVANE<br>RESEARCH</span>
    </div>

    <div class="contact">
      <p class="contact__name">YOUR NAME</p>
      <p class="contact__title">TITEL</p>
      <p class="contact__address">your address can put here<br>your address can put here</p>
      <ul class="contact__list">
        <li class="contact__item">
          <svg class="contact__icon" viewBox="0 0 16 16" aria-hidden="true">
            <rect width="16" height="16" rx="2" fill="#6a4088"/>
            <path d="M5 3.5c-.8.4-1.3 1.2-1 2.4.6 2.6 2.8 4.9 5.4 5.7 1.1.3 2-.1 2.4-.9l-1.7-1.4-1.1.8C7.7 9.6 6.6 8.4 6.1 7.1l.8-1.1z" fill="#fff"/>
          </svg>
          <span>012 456 789</span>
        </li>
        <li class="contact__item">
          <svg class="contact__icon" viewBox="0 0 16 16" aria-hidden="true">
            <rect width="16" height="16" rx="2" fill="#6a4088"/>
            <rect x="5" y="3" width="6" height="3" fill="#fff"/>
            <rect x="3" y="6.5" width="10" height="4.5" rx="1" fill="#fff"/>
            <rect x="5" y="11.5" width="6" height="1.8" fill="#fff"/>
          </svg>
          <span>012 456 789</span>
        </li>
        <li class="contact__item">
          <svg class="contact__icon" viewBox="0 0 16 16" aria-hidden="true">
            <rect width="16" height="16" rx="2" fill="#6a4088"/>
            <rect x="3" y="4.5" width="10" height="7" fill="none" stroke="#fff" stroke-width="1.2"/>
            <path d="M3 4.5l5 4 5-4" fill="none" stroke="#fff" stroke-width="1.2"/>
          </svg>
          <span>yourname@corvane.com</span>
        </li>
        <li class="contact__item">
          <svg class="contact__icon" viewBox="0 0 16 16" aria-hidden="true">
            <rect width="16" height="16" rx="2" fill="#6a4088"/>
            <circle cx="8" cy="8" r="4.6" fill="none" stroke="#fff" stroke-width="1.1"/>
            <ellipse cx="8" cy="8" rx="2" ry="4.6" fill="none" stroke="#fff" stroke-width="1"/>
            <path d="M3.4 8h9.2" stroke="#fff" stroke-width="1"/>
          </svg>
          <span>www.corvane.com</span>
        </li>
      </ul>
    </div>

    <svg class="front-band" viewBox="0 0 560 40" aria-hidden="true">
      <path d="M0 0H360L384 22H560V40H0Z" fill="#6a4088"/>
      <rect x="388" y="4" width="30" height="30" fill="#6a4088"/>
    </svg>
  </section>

</main>
</body>
</html>
```